Very Simple/Minimal Business Card Design Project

The company operates in the industrial maritime infrastructure sector in Brazil. You can find more information on our website www.navelquor.com.br WE NEED TO LOOK POWERFUL AND SERIOUS
I have attached a copy of the old cards. We would like something more professional / industrial / sexy that also includes the position.

The card can be double sided or not. We would like you to propose as many options.

Thank you
Updates

Many thanks, do let me know if you have any questions. I am under a lot of time pressure to try and have them printed over the next days or so.

Please could you use the following information

for the address: Rua Tapiraçu, 418 - Centro, Rio de Janeiro, 20135-070, Brasil

for the mobile: +55 21 8372 9041
for the landline: +55 21 4067 3859

and position:  Diretor Geral

Thakn you

Target Market(s)

Shipowners, bankers, industrial companies

Industry/Entity Type

Industrial

Requirements
Must have
• POWERFUL
SERIOUS
SOLID
BIG CORPORATION

```html
<!DOCTYPE html>
<html lang="pt-BR">
<head>
<meta charset="utf-8">
<title>Navelquor – Business Card</title>
<link rel="stylesheet" href="https://fonts.googleapis.com/css2?family=Archivo:wght@800&family=Michroma&family=Arimo:wght@400&display=swap">
<style>
  :root {
    --stage-light: #f4f4f5;
    --stage-dark: #cfd0d2;
    --card-black: #030303;
    --card-edge: #3c3c3c;
    --texture-grey: #4a4a4c;
    --brand-green: #1f9a50;
    --logo-silver: #dcdcdc;
    --text-white: #f2f2f2;
    --text-grey: #8c8c8c;
  }
  * { margin: 0; padding: 0; box-sizing: border-box; }
  html, body { width: 1200px; height: 900px; overflow: hidden; }
  body {
    position: relative;
    background: radial-gradient(ellipse at 50% 45%, var(--stage-light) 0%, var(--stage-dark) 100%);
    font-family: "Arimo", Arial, sans-serif;
  }
  .card {
    position: absolute;
    left: 284px;
    width: 632px;
    height: 385px;
    background: var(--card-black);
    border: 1px solid var(--card-edge);
    overflow: hidden;
  }
  .card--front { top: 35px; border-top-right-radius: 32px; }
  .card--back { top: 452px; border-top-left-radius: 32px; }

  .card__texture {
    position: absolute;
    inset: 0;
  }
  .card--front .card__texture {
    background: linear-gradient(105deg, transparent 44%, rgba(74,74,76,0.35) 60%, var(--texture-grey) 100%);
  }
  .card--back .card__texture {
    background: linear-gradient(100deg, transparent 50%, rgba(74,74,76,0.35) 66%, var(--texture-grey) 100%);
  }

  .brand {
    position: absolute;
    left: 47px;
    top: 38px;
    display: flex;
    align-items: center;
    gap: 12px;
  }
  .brand__square {
    width: 98px;
    height: 98px;
    background: var(--brand-green);
    border-radius: 6px;
  }
  .brand__name {
    font-family: "Archivo", "Arial Black", sans-serif;
    font-weight: 800;
    font-size: 68px;
    line-height: 1;
    color: var(--logo-silver);
    white-space: nowrap;
  }

  .holder {
    position: absolute;
    left: 0;
    right: 0;
    top: 245px;
    text-align: center;
    font-family: "Michroma", "Eurostile", sans-serif;
  }
  .holder__name {
    font-size: 19px;
    letter-spacing: 3px;
    color: var(--text-white);
  }
  .holder__first { color: var(--brand-green); margin-right: 10px; }
  .holder__role {
    margin-top: 4px;
    font-size: 11px;
    letter-spacing: 8px;
    color: var(--text-grey);
  }

  .contact {
    position: absolute;
    left: 64px;
    top: 72px;
    list-style: none;
    color: var(--text-white);
    font-size: 17px;
  }
  .contact__item {
    display: flex;
    align-items: flex-start;
    gap: 10px;
    margin-bottom: 8px;
  }
  .contact__item--address { margin-bottom: 10px; line-height: 24px; }
  .contact__item span { line-height: 25px; }
  .contact__icon {
    width: 28px;
    height: 25px;
    flex: none;
    fill: var(--brand-green);
    stroke: var(--brand-green);
  }
</style>
</head>
<body>

<section class="card card--front">
  <div class="card__texture" role="img" aria-label="Perforated metal texture fading in from the right"></div>
  <div class="brand">
    <div class="brand__square"></div>
    <div class="brand__name">NAVELQUOR</div>
  </div>
  <div class="holder">
    <p class="holder__name"><span class="holder__first">RAFAEL</span>MONTEVERDE</p>
    <p class="holder__role">DIRECTOR GENERAL</p>
  </div>
</section>

<section class="card card--back">
  <div class="card__texture" role="img" aria-label="Perforated metal texture fading in from the right"></div>
  <ul class="contact">
    <li class="contact__item contact__item--address">
      <svg class="contact__icon" viewBox="0 0 28 34" style="height:34px" aria-hidden="true">
        <path d="M14 2a9 9 0 0 0-9 9c0 7 9 21 9 21s9-14 9-21a9 9 0 0 0-9-9z" stroke="none"/>
      </svg>
      <span>Rua Tapiraçu, 418 - Centro,<br>Rio de Janeiro,<br>20135-070,<br>Brasil</span>
    </li>
    <li class="contact__item">
      <svg class="contact__icon" viewBox="0 0 28 25" aria-hidden="true">
        <path d="M3 8c0-3 5-5 11-5s11 2 11 5v2h-5V7H8v3H3z" stroke="none"/>
        <rect x="6" y="11" width="16" height="11" rx="2" stroke="none"/>
        <circle cx="14" cy="16.5" r="3" fill="#030303" stroke="none"/>
      </svg>
      <span>+55 21 4067 3859</span>
    </li>
    <li class="contact__item">
      <svg class="contact__icon" viewBox="0 0 28 30" style="height:30px" aria-hidden="true">
        <rect x="7" y="1.5" width="14" height="27" rx="2.5" fill="none" stroke-width="2"/>
        <line x1="9" y1="23" x2="19" y2="23" stroke-width="1.5"/>
        <circle cx="14" cy="26" r="1.2" stroke="none"/>
      </svg>
      <span>+55 21 8372 9041</span>
    </li>
    <li class="contact__item">
      <svg class="contact__icon" viewBox="0 0 28 25" aria-hidden="true">
        <rect x="2" y="4" width="24" height="17" fill="none" stroke-width="2"/>
        <path d="M2 4l12 10 12-10M2 21l9-8M26 21l-9-8" fill="none" stroke-width="1.8"/>
      </svg>
      <span>rafael@navelquor.com.br</span>
    </li>
    <li class="contact__item">
      <svg class="contact__icon" viewBox="0 0 28 28" style="height:28px" aria-hidden="true">
        <circle cx="14" cy="14" r="12" fill="none" stroke-width="2"/>
        <ellipse cx="14" cy="14" rx="5" ry="12" fill="none" stroke-width="1.6"/>
        <path d="M2 14h24M4 8h20M4 20h20" fill="none" stroke-width="1.6"/>
      </svg>
      <span>www.navelquor.com.br</span>
    </li>
  </ul>
</section>

</body>
</html>
```